TLPB Business Card Design

Business card for sole operator professional civil and traffic engineer.
Clients are developers and planners who require assistance with traffic strategic master planning advice and design development for access and infrastructure associated with the development.
Colours already in use are greens for the business name and black for other legend. The attached file shows the letterhead template which is currently in use.
Target Market(s)
Professional Clients in development industry
Most clients known to the Principal and card is mostly required to allow ongoing contact
Industry/Entity Type
Business
Contact Information for Business Card
DESMOND HALVERTON CONSULTING SERVICES
ABN 37 818 502 194
PO Box 871 KERRAWAY NSW 2619
Desmond Halverton 0431 558 906
desmond.halverton@quillmarsh.net

```html
<!DOCTYPE html>
<html lang="en">
<head>
<meta charset="utf-8">
<title>TLPB Business Card Options</title>
<link href="https://fonts.googleapis.com/css2?family=Montserrat:wght@400;600;700;800&display=swap" rel="stylesheet">
<style>
  :root {
    --page: #ffffff;
    --green-bright: #8dc63f;
    --green-mid: #78ad34;
    --green-deep: #5f9428;
    --green-mark: #a6d65a;
    --olive: #6b7865;
    --silver-light: #f4f4f4;
    --silver-dark: #c9c9c9;
    --ink: #1d1d1d;
    --white: #ffffff;
    --label: #7aa63a;
  }
  * { box-sizing: border-box; margin: 0; padding: 0; }
  html, body { width: 1200px; height: 566px; overflow: hidden; background: var(--page); }
  body { font-family: "Montserrat", Arial, sans-serif; position: relative; }

  .option { position: absolute; top: 0; width: 600px; height: 566px; }
  .option--one { left: 0; }
  .option--two { left: 600px; }

  .option-number {
    position: absolute; left: 40px; top: 390px;
    font-size: 160px; font-weight: 800; line-height: 1; color: var(--label);
  }

  .card {
    position: absolute; top: 120px; width: 270px; height: 165px;
    border-radius: 2px; overflow: hidden;
    box-shadow: 0 3px 10px rgba(0,0,0,0.18);
  }
  .card--back { left: 20px; }
  .card--front { left: 310px; }

  /* information side */
  .card--olive { background: var(--olive); color: var(--white); }
  .card--silver { background: radial-gradient(circle at 40% 40%, var(--silver-light), var(--silver-dark)); color: var(--ink); }

  .info-brand { position: absolute; left: 18px; top: 16px; }
  .info-brand__name { font-size: 22px; font-weight: 800; color: var(--green-bright); letter-spacing: 0.5px; line-height: 1; }
  .info-brand__caption { margin-top: 4px; font-size: 4.6px; font-weight: 600; letter-spacing: 0.8px; color: var(--green-bright); }

  .info-rule { position: absolute; left: 18px; right: 18px; top: 70px; height: 1px; background: var(--green-bright); }

  .info-details { position: absolute; left: 110px; top: 78px; font-size: 7px; line-height: 1.6; }
  .info-details__name { font-size: 8.5px; font-weight: 700; letter-spacing: 0.6px; color: var(--green-bright); margin-bottom: 2px; }
  .info-line { display: flex; align-items: center; gap: 4px; }
  .info-line svg { width: 7px; height: 7px; fill: var(--green-bright); flex: none; }
  .card--silver .info-line span { color: var(--green-mid); }
  .info-abn { margin-top: 5px; font-weight: 600; }

  /* brand side */
  .card--green { background: linear-gradient(135deg, var(--green-bright), var(--green-deep)); }
  .card__texture { position: absolute; inset: 0;
    background: radial-gradient(circle at 70% 30%, rgba(255,255,255,0.14), transparent 55%); }
  .front-brand { position: absolute; inset: 0; display: flex; flex-direction: column; align-items: center; justify-content: center; }
  .front-brand__name { font-size: 54px; font-weight: 800; color: var(--green-mark); line-height: 1; letter-spacing: 1px; }
  .front-brand__caption { margin-top: 8px; font-size: 7px; font-weight: 600; letter-spacing: 1.4px; color: var(--white); }
</style>
</head>
<body>

<svg width="0" height="0" style="position:absolute">
  <defs>
    <symbol id="icon-pin" viewBox="0 0 10 10"><path d="M5 0a3.5 3.5 0 0 0-3.5 3.5C1.5 6 5 10 5 10s3.5-4 3.5-6.5A3.5 3.5 0 0 0 5 0zm0 5a1.5 1.5 0 1 1 0-3 1.5 1.5 0 0 1 0 3z"/></symbol>
    <symbol id="icon-phone" viewBox="0 0 10 10"><path d="M2 0h6a1 1 0 0 1 1 1v8a1 1 0 0 1-1 1H2a1 1 0 0 1-1-1V1a1 1 0 0 1 1-1zm.5 1.5v6h5v-6z"/></symbol>
    <symbol id="icon-mail" viewBox="0 0 10 10"><path d="M0 2h10v6H0zm1 1v.3l4 2.5 4-2.5V3z"/></symbol>
  </defs>
</svg>

<section class="option option--one">
  <article class="card card--back card--olive">
    <div class="info-brand">
      <div class="info-brand__name">TLPB</div>
      <div class="info-brand__caption">DESMOND HALVERTON CONSULTING SERVICES</div>
    </div>
    <div class="info-rule"></div>
    <div class="info-details">
      <div class="info-details__name">DESMOND HALVERTON</div>
      <div class="info-line"><svg><use href="#icon-pin"/></svg>PO Box 871 KERRAWAY NSW 2619</div>
      <div class="info-line"><svg><use href="#icon-phone"/></svg>0431 558 906</div>
      <div class="info-line"><svg><use href="#icon-mail"/></svg>desmond.halverton@quillmarsh.net</div>
      <div class="info-abn">ABN 37 818 502 194</div>
    </div>
  </article>
  <article class="card card--front card--green">
    <div class="card__texture" role="img" aria-label="Soft green swirl background texture"></div>
    <div class="front-brand">
      <div class="front-brand__name">TLPB</div>
      <div class="front-brand__caption">DESMOND HALVERTON CONSULTING SERVICES</div>
    </div>
  </article>
  <div class="option-number">1</div>
</section>

<section class="option option--two">
  <article class="card card--back card--silver">
    <div class="info-brand">
      <div class="info-brand__name">TLPB</div>
      <div class="info-brand__caption">DESMOND HALVERTON CONSULTING SERVICES</div>
    </div>
    <div class="info-rule"></div>
    <div class="info-details">
      <div class="info-details__name">DESMOND HALVERTON</div>
      <div class="info-line"><svg><use href="#icon-pin"/></svg><span>PO Box 871 KERRAWAY NSW 2619</span></div>
      <div class="info-line"><svg><use href="#icon-phone"/></svg><span>0431 558 906</span></div>
      <div class="info-line"><svg><use href="#icon-mail"/></svg><span>desmond.halverton@quillmarsh.net</span></div>
      <div class="info-abn">ABN 37 818 502 194</div>
    </div>
  </article>
  <article class="card card--front card--green">
    <div class="card__texture" role="img" aria-label="Soft green swirl background texture"></div>
    <div class="front-brand">
      <div class="front-brand__name">TLPB</div>
      <div class="front-brand__caption">DESMOND HALVERTON CONSULTING SERVICES</div>
    </div>
  </article>
  <div class="option-number">2</div>
</section>

</body>
</html>
```